"Velvet Ember" sexual performance enhancement pill bottle label needed.

This should be interesting...

I am starting a line of sexual performance enhancement products. This will be the first of several products basically. Keep in mind, I am the type of business person to stay with one company for years if they provide me with quality work.

This particular product is a male sexual performance pill. The name of the product is "Velvet Ember." The packaging of the pills are a black bottle with a white top. Label on the product example would be perfect but at a minimum I have attached a "template" for your guidance.

Some of the technical aspects of this are as follows:

-File Format: Illustrator CS6 is preferred. (Winner must provide artwork in layer and can not flatten artwork.)
-Resolution: 300 dpi minimum
-Bleed: 1/16th (0.0625") inch from edge of label
-Color Mode: CMYK only or must be converted to CMYK for final production

Lastly, this is your project as a designer, artist, creator, this is essentially a piece of you that will be sold and known by thousands of people. I have no color scheme that I prefer, just use the template and follow the layout. If you have any further questions, please feel free to contact me at any time.
Updates

Quick note on the product and what it does: -Powerful, long lasting, harder erections -Works in a minutes and last for hours -Enhances sexual desire and drive Thank you for your ideas...

Project Deadline Extended
Reason: We decided to extent the project for a few more days to let the last few concepts come in. So far things are looking really good and we definitely have seen some amazing designs. Thank you for your hard work and amazing creativity. Looking forward to seeing what we have come in the next couple of day. Very respectfully, Doran

ONLY THREE DAYS LEFT!!!! Please submit your ideas as soon as possible. And as always, thank you for your help!!! V/r, Doran

Industry/Entity Type

Graphic Design

```html
<!DOCTYPE html>
<html lang="en">
<head>
<meta charset="utf-8">
<title>Velvet Ember – Bottle Label</title>
<link href="https://fonts.googleapis.com/css2?family=Open+Sans:ital,wght@0,400;0,600;0,700;1,700&family=Montserrat:wght@600;700&family=Roboto+Condensed:wght@400;700&display=swap" rel="stylesheet">
<style>
  :root {
    --ink: #000000;
    --paper: #ffffff;
    --royal: #1f3f86;
    --royal-deep: #142a5c;
    --royal-light: #3b6bb3;
    --copper: #a65a25;
    --gold: #e8c25a;
    --gold-pale: #fff6d8;
    --caption: #f2f2f2;
  }
  * { margin: 0; padding: 0; box-sizing: border-box; }
  html, body { width: 1200px; height: 1000px; overflow: hidden; background: var(--paper); }
  body { position: relative; font-family: "Open Sans", Arial, sans-serif; color: var(--paper); }

  .label {
    position: absolute; left: 16px; top: 265px; width: 1165px; height: 470px;
    background: var(--ink); overflow: hidden;
  }
  .backdrop-art {
    position: absolute; left: 250px; top: 0; width: 620px; height: 412px;
    background:
      radial-gradient(ellipse 120px 200px at 440px 170px, rgba(31,63,134,.85), rgba(31,63,134,0) 70%),
      radial-gradient(ellipse 260px 220px at 180px 160px, rgba(60,60,60,.55), rgba(0,0,0,0) 75%);
  }

  .usage {
    position: absolute; left: 32px; top: 30px; width: 313px;
    font-family: "Roboto Condensed", Arial, sans-serif;
    font-size: 10.6px; line-height: 1.3; text-align: justify;
  }
  .usage p { margin-bottom: 5px; }
  .usage strong { font-weight: 700; }
  .usage .storage { font-weight: 700; font-size: 11.4px; line-height: 1.25; }
  .fda-note {
    margin-top: 8px; padding: 4px 8px; font-size: 10px; line-height: 1.3;
    background: linear-gradient(90deg, var(--royal) 60%, var(--royal-light));
    border: 1px solid #4a72b8;
  }
  .maker { position: absolute; left: 38px; top: 298px; }
  .maker .for { font-style: italic; font-weight: 700; font-size: 14px; }
  .maker .company { font-weight: 700; font-size: 14px; margin-top: 2px; }

  .category {
    position: absolute; left: 379px; top: 52px; width: 400px; text-align: center;
    font-size: 27px; font-weight: 600; letter-spacing: .5px;
  }
  .mark-dot {
    position: absolute; left: 434px; top: 80px; width: 290px; height: 290px; border-radius: 50%;
    background: radial-gradient(circle at 50% 45%, var(--royal-light) 0%, var(--royal) 55%, var(--royal-deep) 100%);
  }
  .brand-name {
    position: absolute; left: 379px; top: 288px; width: 400px; text-align: center;
    font-size: 46px; font-weight: 700; color: var(--gold);
  }
  .claim {
    position: absolute; left: 379px; top: 370px; width: 400px; text-align: center;
    font-family: "Roboto Condensed", Arial, sans-serif;
    font-size: 17px; line-height: 1.15; color: var(--caption);
  }

  .facts { position: absolute; left: 845px; top: 40px; width: 264px; }
  .facts h2 { font-family: "Montserrat", Arial, sans-serif; font-weight: 700; font-size: 27px; }
  .facts .serving { font-family: "Montserrat", Arial, sans-serif; font-weight: 600; font-size: 12.5px; line-height: 1.35; }
  .facts .rule-thick { height: 5px; background: var(--royal); margin: 4px 0 2px; }
  .facts .head { display: flex; justify-content: space-between; font-size: 11.5px; padding: 3px 0; }
  .facts .rule { height: 2px; background: var(--royal); }
  .facts .blend {
    font-family: "Roboto Condensed", Arial, sans-serif;
    font-size: 11.4px; line-height: 1.4; text-align: justify; padding: 4px 0;
  }
  .facts .blend strong { font-weight: 700; }
  .facts .dv { font-size: 12px; font-weight: 600; margin-top: 10px; }
  .facts .other { font-family: "Roboto Condensed", Arial, sans-serif; font-size: 11px; margin-top: 12px; line-height: 1.3; }
  .site { position: absolute; left: 843px; top: 362px; font-size: 24px; letter-spacing: .3px; }

  .benefit-band {
    position: absolute; left: 0; top: 412px; width: 100%; height: 30px;
    background: linear-gradient(90deg, var(--royal) 0%, #254c95 55%, var(--royal-light) 80%, var(--royal) 100%);
    display: flex; justify-content: center; align-items: center; gap: 36px;
    font-family: "Roboto Condensed", Arial, sans-serif; font-size: 18px;
  }
  .accent-band {
    position: absolute; left: 0; top: 442px; width: 100%; height: 28px;
    background: linear-gradient(90deg, var(--copper) 0%, #c88a3a 45%, var(--gold-pale) 68%, var(--paper) 75%, var(--gold-pale) 82%, var(--gold) 100%);
  }
</style>
</head>
<body>
  <section class="label">
    <div class="backdrop-art" role="img" aria-label="Dark swirling ornaments with a blue silhouette of a woman"></div>

    <div class="usage">
      <p><strong>SUGGESTED USE:</strong> As a dietary supplement, take two (2) capsules 1 hour before physical activity, or as directed by your health care professional. Do not exceed two (2) capsules daily.</p>
      <p><strong>CAUTION:</strong> Do not exceed recommended dose. This product is not intended for pregnant or nursing mothers, children under the age of 18, or individuals taking prescription drugs. Discontinue use immediately if nausea, sleeplessness, or nervousness occur. Do not take this product if you have a known medical condition including high blood pressure, diabetes, any cardiovascular disorder, heart disease, hyperthyroidism or are taking anti-depressant medication. If you have questions about the advisability of taking this product consult your physician prior to use.</p>
      <p class="storage">KEEP OUT OF THE REACH OF CHILDREN. DO NOT USE IF SAFETY SEAL IS DAMAGED OR MISSING. STORE AT ROOM TEMPERATURE.</p>
      <div class="fda-note">* These statements have not been evaluated by the Food and Drug Administration. This product is not intended to diagnose, treat, cure or prevent any disease.</div>
    </div>

    <div class="maker">
      <div class="for">Manufactured Exclusively For:</div>
      <div class="company">COMPANY INFO</div>
    </div>

    <div class="category">MALE ENHANCEMENT</div>
    <div class="mark-dot"></div>
    <div class="brand-name">Velvet Ember</div>
    <div class="claim">Works in a minutes and &nbsp;last for hours Enhances<br>Sexual Desire and Drive</div>

    <div class="facts">
      <h2>Supplement Facts</h2>
      <div class="serving">Serving Size: 2 Capsules<br>Servings Per Container: 30</div>
      <div class="rule-thick"></div>
      <div class="head"><span>Amount Per Serving</span><span>% Daily Value</span></div>
      <div class="rule"></div>
      <div class="blend"><strong>VE-Rx™ Proprietary Formula &nbsp;1,560 mg †</strong> Horny Goat Weed (herb powder), Maca (herb powder), Mucuna Pruriens (L-Dopa), Polypodium Vulgare (herb powder), Yohimbe Bark (herb powder), Saw Palmetto (herb powder), Muira Puama (herb powder), Arginine (L-Arginine hydrochloride), Panax Ginseng (herb powder)</div>
      <div class="rule"></div>
      <div class="dv">† % Daily Value not established</div>
      <div class="other"><strong>Other Ingredients:</strong> Gelatin, Magnesium Stearate, and Calcium Carbonate.</div>
    </div>
    <div class="site">www.VelvetEmberPill.com</div>

    <div class="benefit-band"><span>Powerful</span><span>Long Lasting</span><span>Harder Erections</span></div>
    <div class="accent-band"></div>
  </section>
</body>
</html>
```